Brightwell Pictures Business Card

Hello,

i would like to have a dynamic, creative but tasteful card, colour used, front and back. I have attached a sample card that I liked very much from another individual to give you an idea of the theme/approach, but not colour. Ideally the graphic elements of the Brightwell Logo are brought into the design.

Target Market(s)

North America

Industry/Entity Type

Film Production

Contact Information for Business Card

Mirela Vantasch
President/Founder
Brightwell Pictures Inc.
587 914 3362
mirela@brightwellpix.tv

Font styles to use
Sans Serif

Colors
6b449b
5c5c5c
fdfdfd
000000

Requirements
Must have
• Logo, name, Company name, email and cell number. no Address line to be included.
Should not have
• any unrelated GFX elements, serif fonts

```html
<!DOCTYPE html>
<html lang="en">
<head>
<meta charset="utf-8">
<title>Brightwell Pictures Business Card</title>
<link rel="stylesheet" href="https://fonts.googleapis.com/css2?family=Open+Sans:wght@400;600;800&display=swap">
<style>
  :root {
    --stage: #1b1b1b;
    --card: #0d0d0d;
    --card-edge: #222222;
    --purple: #6b449b;
    --grey: #5c5c5c;
    --white: #fdfdfd;
    --black: #000000;
    --divider: #2a2a2a;
  }
  * { box-sizing: border-box; margin: 0; padding: 0; }
  html, body {
    width: 1200px;
    height: 900px;
    overflow: hidden;
    background: var(--stage);
    font-family: "Open Sans", Arial, sans-serif;
  }
  .stage {
    position: relative;
    width: 1200px;
    height: 900px;
  }
  .card {
    position: absolute;
    top: 300px;
    width: 510px;
    height: 300px;
    background: var(--card);
    border-radius: 22px;
    border: 1px solid var(--card-edge);
    box-shadow: 0 18px 40px rgba(0,0,0,0.55);
  }
  /* Contact side */
  .card--contact { left: 60px; }
  .brand-mark {
    position: absolute;
    left: 34px;
    top: 0;
    width: 200px;
    height: 100%;
    display: flex;
    flex-direction: column;
    align-items: center;
    justify-content: center;
    gap: 14px;
  }
  .brand-mark__dot {
    width: 110px;
    height: 110px;
    border-radius: 50%;
    background: var(--purple);
  }
  .brand-mark__name {
    color: var(--purple);
    font-weight: 800;
    font-size: 28px;
    letter-spacing: -0.5px;
  }
  .card__divider {
    position: absolute;
    left: 262px;
    top: 40px;
    bottom: 40px;
    width: 1px;
    background: var(--divider);
  }
  .contact {
    position: absolute;
    left: 286px;
    top: 78px;
    color: var(--white);
    font-size: 13.5px;
    line-height: 1.45;
  }
  .contact__name {
    color: var(--purple);
    font-weight: 600;
    font-size: 14px;
    letter-spacing: 0.6px;
    text-transform: uppercase;
  }
  .contact__title { margin-bottom: 22px; }
  .contact__company { margin-bottom: 8px; }
  .contact__line {
    display: flex;
    align-items: center;
    gap: 8px;
  }
  .contact__icon { width: 12px; height: 12px; flex: none; }
  /* Logo side */
  .card--logo { left: 630px; }
  .wordmark {
    position: absolute;
    inset: 0;
    display: flex;
    align-items: center;
    justify-content: center;
    color: #d9d9d9;
    font-weight: 800;
    font-size: 44px;
    letter-spacing: -1px;
  }
</style>
</head>
<body>
<main class="stage">
  <section class="card card--contact">
    <div class="brand-mark">
      <span class="brand-mark__dot"></span>
      <span class="brand-mark__name">Brightwell</span>
    </div>
    <div class="card__divider"></div>
    <div class="contact">
      <p class="contact__name">Mirela Vantasch</p>
      <p class="contact__title">President/Founder</p>
      <p class="contact__company">Brightwell Pictures Inc.</p>
      <p class="contact__line">
        <svg class="contact__icon" viewBox="0 0 12 12" aria-hidden="true">
          <rect x="2.5" y="0.5" width="7" height="11" rx="1.2" fill="none" stroke="#6b449b" stroke-width="1.4"/>
          <circle cx="6" cy="9.5" r="0.8" fill="#6b449b"/>
        </svg>
        587 914 3362
      </p>
      <p class="contact__line">
        <svg class="contact__icon" viewBox="0 0 12 12" aria-hidden="true">
          <rect x="0" y="2" width="12" height="8.5" fill="#6b449b"/>
          <path d="M0.5 2.5 L6 7 L11.5 2.5" fill="none" stroke="#0d0d0d" stroke-width="1"/>
        </svg>
        mirela@brightwellpix.tv
      </p>
    </div>
  </section>
  <section class="card card--logo">
    <div class="wordmark">Brightwell Pictures</div>
  </section>
</main>
</body>
</html>
```